Modern looking signage for dental office.

Exterior signage for passing cars
Target Market(s)
Cars passing by
Font styles to use
Sans Serif
Colors
3276b5
Requirements
Must have
- Logo
- OPEN ON SUTURDAY AND SUNDAY
- NIGHT CLINIC AVAILABLE
- PLEASE USE THE FONT TYPE IN FILE 4 UPLOADED BELOW.
- (482) 730-2964
- Modern looking

```html
<!DOCTYPE html>
<html lang="en">
<head>
<meta charset="utf-8">
<title>Peak Dental – Exterior Signage</title>
<link href="https://fonts.googleapis.com/css2?family=PT+Sans+Narrow:wght@400;700&family=Open+Sans:wght@400&display=swap" rel="stylesheet">
<style>
  :root {
    --backdrop: #232323;
    --sign-white: #ffffff;
    --teal: #0e849c;
    --brand-blue: #2a77b6;
    --ink-gray: #555555;
    --rule-gray: #4d4a4a;
    --label-white: #f2f2f2;
  }
  * { margin: 0; padding: 0; box-sizing: border-box; }
  html, body { width: 1200px; height: 895px; overflow: hidden; }
  body {
    position: relative;
    background: var(--backdrop);
    font-family: "PT Sans Narrow", "Arial Narrow", sans-serif;
  }
  .sign {
    position: absolute;
    background: var(--sign-white);
    box-shadow: 0 2px 8px rgba(0,0,0,0.6);
    overflow: hidden;
  }
  .sign svg { position: absolute; inset: 0; }
  .sign .line {
    position: absolute; left: 0; width: 100%;
    text-align: center; white-space: nowrap;
    line-height: 1;
  }
  .brand-name { color: var(--ink-gray); font-weight: 400; letter-spacing: 0.02em; }
  .tagline { color: var(--ink-gray); font-weight: 400; }
  .offer { color: var(--sign-white); font-weight: 700; }
  .phone { color: var(--ink-gray); font-weight: 400; }
  .brand-dot, .phone-badge {
    position: absolute; border: 1.5px solid var(--ink-gray); border-radius: 50%;
  }
  .phone-badge svg { position: absolute; inset: 0; }

  /* square sign */
  .sign-square { left: 384px; top: 14px; width: 362px; height: 365px; }
  .sign-square .brand-dot { left: 148px; top: 14px; width: 66px; height: 66px; }
  .sign-square .brand-name { top: 94px; font-size: 44px; }
  .sign-square .tagline { top: 134px; font-size: 15px; }
  .sign-square .offer-1 { top: 196px; font-size: 25px; }
  .sign-square .offer-2 { top: 226px; font-size: 25px; }
  .sign-square .phone-badge { left: 162px; top: 282px; width: 38px; height: 38px; }
  .sign-square .phone { top: 321px; font-size: 32px; }

  /* wide sign */
  .sign-wide { left: 200px; top: 390px; width: 730px; height: 490px; }
  .sign-wide .brand-dot { left: 134px; top: 35px; width: 98px; height: 100px; }
  .sign-wide .brand-row { position: absolute; left: 244px; top: 56px; }
  .sign-wide .brand-name { position: static; font-size: 72px; line-height: 1; white-space: nowrap; }
  .sign-wide .tagline { left: 278px; width: auto; top: 119px; font-size: 25px; text-align: left; }
  .sign-wide .offer-1 { top: 230px; font-size: 54px; }
  .sign-wide .offer-2 { top: 279px; font-size: 54px; }
  .sign-wide .phone-badge { left: 166px; top: 397px; width: 66px; height: 66px; }
  .sign-wide .phone { left: 250px; width: auto; top: 400px; font-size: 62px; text-align: left; }

  .ratio-label {
    position: absolute; color: var(--label-white);
    font-family: "Open Sans", Arial, sans-serif; font-weight: 400; line-height: 1;
  }
  .ratio-square { left: 776px; top: 186px; font-size: 66px; }
  .ratio-wide { left: 960px; top: 624px; font-size: 70px; }
</style>
</head>
<body>

<section class="sign sign-square">
  <svg viewBox="0 0 362 365" width="362" height="365">
    <path d="M0 154 Q181 200 362 154 L362 294 Q181 248 0 294 Z" fill="var(--teal)"/>
    <path d="M0 149 Q181 196 362 149" fill="none" stroke="var(--rule-gray)" stroke-width="1.5"/>
    <path d="M0 298 Q181 252 362 298" fill="none" stroke="var(--rule-gray)" stroke-width="1.5"/>
  </svg>
  <span class="brand-dot"></span>
  <div class="line brand-name">PEAK DENTAL</div>
  <div class="line tagline">MODERN GENERAL DENTISTRY</div>
  <div class="line offer offer-1">OPEN ON SUTURDAY AND SUNDAY</div>
  <div class="line offer offer-2">NIGHT CLINIC AVAILABLE</div>
  <span class="phone-badge">
    <svg viewBox="0 0 38 38"><path d="M12 10 l4 -1 l3 6 l-3 2 q2 5 7 7 l2 -3 l6 3 l-1 4 q-3 3 -9 0 q-8 -5 -10 -12 q-1 -4 1 -6 z" fill="none" stroke="var(--brand-blue)" stroke-width="1.4" stroke-linejoin="round"/></svg>
  </span>
  <div class="line phone">(482) 730-2964</div>
</section>

<section class="sign sign-wide">
  <svg viewBox="0 0 730 490" width="730" height="490">
    <path d="M0 150 Q365 246 730 150 L730 406 Q365 318 0 406 Z" fill="var(--brand-blue)"/>
    <path d="M0 144 Q365 242 730 144" fill="none" stroke="var(--rule-gray)" stroke-width="3"/>
    <path d="M0 412 Q365 324 730 412" fill="none" stroke="var(--rule-gray)" stroke-width="3"/>
  </svg>
  <span class="brand-dot"></span>
  <div class="brand-row"><div class="brand-name">PEAK DENTAL</div></div>
  <div class="line tagline">MODERN GENERAL DENTISTRY</div>
  <div class="line offer offer-1">OPEN ON SATURDAY AND SUNDAY</div>
  <div class="line offer offer-2">NIGHT CLINIC AVAILABLE</div>
  <span class="phone-badge">
    <svg viewBox="0 0 66 66"><path d="M20 17 l7 -2 l5 10 l-5 4 q4 9 12 12 l4 -5 l10 5 l-2 7 q-5 5 -15 0 q-14 -8 -18 -21 q-1 -7 2 -10 z" fill="none" stroke="var(--brand-blue)" stroke-width="2.2" stroke-linejoin="round"/></svg>
  </span>
  <div class="line phone">(482) 730-2964</div>
</section>

<div class="ratio-label ratio-square">1:1</div>
<div class="ratio-label ratio-wide">2:1</div>

</body>
</html>
```